Tourism Advertisement in County Map

Our county is producing a map and I would like to place a half panel ad in it promoting our tourism opportunities. The ad size is 3 1/2" w by 4" h. We are a rural community with lots of outdoor recreational opportunities and a state museum. I will attached a few photos that represent our community. I have no idea how I want the ad to look! I am fine with stock photography as long as it "could" be from my community. Included on the ad I would like our phone number, 910-587-2046 and website, www.thebrantleychamber.example.

We have used a "tagline" of Explore Brantley in previous advertisements. I have included an image of the front cover of the map which shows some of things we promote. I have also included our logo, though it does not have to be used. It can but it is not a requirement.

Our main tourism attractions are:

NC Gallery of Earth Studies at Pinebrook
Lake Tarrowin-boating, sailing, etc.
The Tarrowin and Hollis Rivers, kayaking, canoeing, etc.
Hunting and Fishing

Industry/Entity Type

Tourism

Colors

Designer to choose colors to be used in the design.

Requirements
Must have
• I have no "must haves"!

```html
<!DOCTYPE html>
<html lang="en">
<head>
<meta charset="utf-8">
<title>Explore Brantley – Tourism Ad</title>
<link rel="stylesheet" href="https://fonts.googleapis.com/css2?family=Lato:ital,wght@0,400;0,700;1,400&family=Oswald:wght@500&display=swap">
<style>
  :root {
    --page-bg: #e6e7e9;
    --navy: #0b4a83;
    --accent-blue: #2c86d6;
    --band-grey: #c8cbcf;
    --band-text: #172a44;
    --white: #ffffff;
    --bullet: #3fa9f0;
    --chamber-blue: #27378c;
  }
  * { box-sizing: border-box; margin: 0; padding: 0; }
  html, body {
    width: 1200px; height: 904px; overflow: hidden;
    background: var(--page-bg);
    font-family: "Lato", sans-serif;
  }
  .ad {
    position: absolute; left: 196px; top: 52px;
    width: 822px; height: 720px;
    overflow: hidden; background: var(--white);
  }
  .ad-shapes { position: absolute; inset: 0; }
  .headline {
    position: absolute; left: 59px; top: 62px;
    color: var(--white); font-size: 43px; line-height: 48px; font-weight: 400;
  }
  .headline .place { display: block; font-weight: 700; font-size: 50px; line-height: 54px; }
  .section-band {
    position: absolute; left: 0; top: 238px; width: 378px; height: 36px;
    background: var(--band-grey); color: var(--band-text);
    font-size: 25px; line-height: 36px; padding-left: 44px; letter-spacing: 0.3px;
  }
  .attractions {
    position: absolute; left: 62px; top: 290px; width: 300px;
    list-style: none; color: var(--white); font-size: 21px; line-height: 23px;
  }
  .attractions .place-name { padding-left: 24px; }
  .attractions .activity {
    position: relative; padding-left: 24px; font-style: italic; margin: 6px 0;
  }
  .attractions .activity::before {
    content: ""; position: absolute; left: 2px; top: 8px;
    width: 10px; height: 10px; border-radius: 50%; background: var(--bullet);
  }
  .attractions .place-name + .activity { margin-top: 10px; }
  .attractions .activity + .place-name { margin-top: 10px; }
  .attractions .activity.last { margin-top: 10px; }
  .call {
    position: absolute; left: 97px; top: 608px;
    color: var(--white); font-family: "Oswald", sans-serif; font-weight: 500;
    font-size: 38px; line-height: 48px;
  }
  .website {
    position: absolute; left: 64px; top: 657px;
    color: var(--white); font-size: 21px; letter-spacing: 0.3px;
  }
  .chamber {
    position: absolute; left: 520px; top: 566px; width: 290px;
    text-align: center; color: var(--chamber-blue); font-weight: 700;
  }
  .chamber-dot {
    display: block; width: 56px; height: 56px; border-radius: 50%;
    background: var(--accent-blue); margin: 0 auto 18px;
  }
  .chamber-name { display: block; font-size: 20px; line-height: 22px; }
  .chamber-sub { display: block; font-size: 12px; letter-spacing: 2.6px; line-height: 16px; }
</style>
</head>
<body>
  <div class="ad">
    <svg class="ad-shapes" width="822" height="720" viewBox="0 0 822 720">
      <defs>
        <linearGradient id="sceneTones" x1="0" y1="0" x2="0" y2="1">
          <stop offset="0" stop-color="#5d9444"/>
          <stop offset="0.32" stop-color="#4b7a3a"/>
          <stop offset="0.42" stop-color="#66715a"/>
          <stop offset="0.6" stop-color="#8d9384"/>
          <stop offset="0.82" stop-color="#ffffff"/>
        </linearGradient>
      </defs>
      <rect class="river-scene" x="340" y="0" width="482" height="720" fill="url(#sceneTones)"
            role="img" aria-label="Kayakers paddling on a tree-lined river"/>
      <path class="curve-accent" d="M535,0 Q221,360 535,720 H0 V0 Z" fill="var(--accent-blue)"/>
      <path class="panel-blue" d="M519,0 Q205,360 519,720 H0 V0 Z" fill="var(--navy)"/>
    </svg>

    <h1 class="headline">Pick a reason<br>to Explore <span class="place">BRANTLEY</span></h1>

    <div class="section-band">TOURISM ATTRACTIONS</div>

    <ul class="attractions">
      <li class="place-name">NC Gallery of Earth Studies at Pinebrook<br>Lake Tarrowin;</li>
      <li class="activity">Boating</li>
      <li class="activity">Sailing</li>
      <li class="place-name">The Tarrowin and<br>Hollis Rivers;</li>
      <li class="activity">Kayaking</li>
      <li class="activity">Canoeing</li>
      <li class="activity last">Hunting and Fishing</li>
    </ul>

    <p class="call">CALL +910-587-2046</p>
    <p class="website">www.thebrantleychamber.example</p>

    <div class="chamber">
      <span class="chamber-dot"></span>
      <span class="chamber-name">BRANTLEY CHAMBER</span>
      <span class="chamber-sub">OF COMMERCE &amp; TOURISM</span>
    </div>
  </div>
</body>
</html>
```